Turn this into a clear and concise

Attached is a screen shot that we currently show to investors from a software program. We need you to illustrate this in a much more professional looking and easy to view and understand way. If we like your style and attention to detail there is more work behind this.
Industry/Entity Type
Software

```html
<!DOCTYPE html>
<html lang="en">
<head>
<meta charset="utf-8">
<title>Intraday Price, Indicator and Volume Chart</title>
<link rel="stylesheet" href="https://fonts.googleapis.com/css2?family=Inter:wght@400;500&display=swap">
<style>
  :root {
    --page: #ffffff;
    --frame-teal: #0b4d5c;
    --panel: #262e3c;
    --grid: #343d4d;
    --divider: #465063;
    --base: #8d97a8;
    --tick: #8d97a8;
    --session-marker: #f2e46b;
    --zero-line: #2f9e55;
    --candle-up: #2fb862;
    --candle-down: #ee4b4b;
    --wick: #b9c1cd;
    --indicator: #ffffff;
    --volume: #f0932b;
    --label: #eef2f7;
    --label-muted: #c3cad6;
  }
  html, body {
    margin: 0;
    padding: 0;
    width: 1200px;
    height: 857px;
    overflow: hidden;
    background: var(--page);
  }
  .chart {
    display: block;
    width: 1200px;
    height: 857px;
    font-family: "Inter", Arial, sans-serif;
  }
  .frame-teal { fill: var(--frame-teal); }
  .panel { fill: var(--panel); }
  .grid line { stroke: var(--grid); stroke-width: 1; }
  .divider { stroke: var(--divider); stroke-width: 1.2; }
  .base-line { stroke: var(--base); stroke-width: 1.2; }
  .zero-line { stroke: var(--zero-line); stroke-width: 1.6; }
  .session-markers line { stroke: var(--session-marker); stroke-width: 1.4; stroke-opacity: 0.85; }
  .axis-ticks line { stroke: var(--tick); stroke-width: 1; }
  .wick { stroke: var(--wick); stroke-width: 1.2; }
  .candle-up { fill: var(--candle-up); }
  .candle-down { fill: var(--candle-down); }
  .indicator-line { fill: none; stroke: var(--indicator); stroke-width: 3.5; stroke-linejoin: round; stroke-linecap: round; }
  .volume-bars rect { fill: var(--volume); }
  .axis-label { fill: var(--label); font-size: 17px; font-weight: 500; }
  .axis-label-minor { fill: var(--label-muted); font-size: 17px; font-weight: 400; }
  .time-label { fill: var(--label); font-size: 17px; font-weight: 500; text-anchor: middle; }
</style>
</head>
<body>
<svg class="chart" viewBox="0 0 1400 1000" xmlns="http://www.w3.org/2000/svg" role="img" aria-label="Intraday candlestick price chart with indicator line and volume bars, 8 AM to 12 PM">
  <rect class="frame-teal" x="71" y="33" width="1264" height="932"/>
  <rect class="panel" x="70" y="33" width="1148" height="877"/>

  <g class="grid">
    <line x1="70" y1="65" x2="1218" y2="65"/><line x1="70" y1="98" x2="1218" y2="98"/>
    <line x1="70" y1="129" x2="1218" y2="129"/><line x1="70" y1="161" x2="1218" y2="161"/>
    <line x1="70" y1="193" x2="1218" y2="193"/><line x1="70" y1="225" x2="1218" y2="225"/>
    <line x1="70" y1="257" x2="1218" y2="257"/><line x1="70" y1="321" x2="1218" y2="321"/>
    <line x1="70" y1="353" x2="1218" y2="353"/><line x1="70" y1="385" x2="1218" y2="385"/>
    <line x1="70" y1="417" x2="1218" y2="417"/><line x1="70" y1="449" x2="1218" y2="449"/>
    <line x1="70" y1="481" x2="1218" y2="481"/><line x1="70" y1="512" x2="1218" y2="512"/>
    <line x1="70" y1="544" x2="1218" y2="544"/><line x1="70" y1="576" x2="1218" y2="576"/>
    <line x1="70" y1="608" x2="1218" y2="608"/><line x1="70" y1="640" x2="1218" y2="640"/>
    <line x1="70" y1="704" x2="1218" y2="704"/><line x1="70" y1="735" x2="1218" y2="735"/>
    <line x1="70" y1="767" x2="1218" y2="767"/><line x1="70" y1="799" x2="1218" y2="799"/>
    <line x1="70" y1="831" x2="1218" y2="831"/>
    <line x1="268" y1="33" x2="268" y2="865"/><line x1="517" y1="33" x2="517" y2="865"/>
    <line x1="767" y1="33" x2="767" y2="865"/><line x1="1018" y1="33" x2="1018" y2="865"/>
  </g>
  <line class="divider" x1="70" y1="289" x2="1218" y2="289"/>
  <line class="zero-line" x1="70" y1="672" x2="1218" y2="672"/>
  <line class="base-line" x1="70" y1="865" x2="1218" y2="865"/>

  <g class="session-markers">
    <line x1="143" y1="33" x2="143" y2="865"/>
    <line x1="392" y1="33" x2="392" y2="865"/>
    <line x1="641" y1="33" x2="641" y2="865"/>
    <line x1="893" y1="33" x2="893" y2="865"/>
    <line x1="1143" y1="33" x2="1143" y2="865"/>
  </g>

  <g class="axis-ticks">
    <line x1="1218" y1="65" x2="1228" y2="65"/><line x1="1218" y1="98" x2="1228" y2="98"/>
    <line x1="1218" y1="129" x2="1228" y2="129"/><line x1="1218" y1="161" x2="1228" y2="161"/>
    <line x1="1218" y1="193" x2="1228" y2="193"/><line x1="1218" y1="225" x2="1228" y2="225"/>
    <line x1="1218" y1="257" x2="1228" y2="257"/><line x1="1218" y1="289" x2="1228" y2="289"/>
    <line x1="1218" y1="321" x2="1228" y2="321"/><line x1="1218" y1="353" x2="1228" y2="353"/>
    <line x1="1218" y1="385" x2="1228" y2="385"/><line x1="1218" y1="417" x2="1228" y2="417"/>
    <line x1="1218" y1="449" x2="1228" y2="449"/><line x1="1218" y1="481" x2="1228" y2="481"/>
    <line x1="1218" y1="512" x2="1228" y2="512"/><line x1="1218" y1="544" x2="1228" y2="544"/>
    <line x1="1218" y1="576" x2="1228" y2="576"/><line x1="1218" y1="608" x2="1228" y2="608"/>
    <line x1="1218" y1="640" x2="1228" y2="640"/><line x1="1218" y1="672" x2="1228" y2="672"/>
    <line x1="1218" y1="704" x2="1228" y2="704"/><line x1="1218" y1="735" x2="1228" y2="735"/>
    <line x1="1218" y1="767" x2="1228" y2="767"/><line x1="1218" y1="799" x2="1228" y2="799"/>
    <line x1="1218" y1="831" x2="1228" y2="831"/>
  </g>

  <g class="axis-labels">
    <text class="axis-label" x="1240" y="71">137’24</text>
    <text class="axis-label-minor" x="1240" y="104">137’20</text>
    <text class="axis-label-minor" x="1240" y="135">137’18</text>
    <text class="axis-label-minor" x="1240" y="167">137’16</text>
    <text class="axis-label-minor" x="1240" y="199">137’14</text>
    <text class="axis-label-minor" x="1240" y="231">137’12</text>
    <text class="axis-label" x="1240" y="263">137’08</text>
    <text class="axis-label" x="1240" y="391">136’28</text>
    <text class="axis-label" x="1240" y="487">136’16</text>
    <text class="axis-label" x="1240" y="550">100</text>
    <text class="axis-label" x="1240" y="678">0</text>
    <text class="axis-label" x="1240" y="741">20,000</text>
    <text class="axis-label" x="1240" y="805">10,000</text>
  </g>

  <g class="candles">
    <line class="wick" x1="105" y1="231" x2="105" y2="283"/><rect class="candle-down" x="99" y="233" width="12" height="44" rx="1.5"/>
    <line class="wick" x1="141" y1="264" x2="141" y2="296"/><rect class="candle-up" x="135" y="268" width="12" height="24" rx="1.5"/>
    <line class="wick" x1="178" y1="270" x2="178" y2="318"/><rect class="candle-up" x="172" y="276" width="12" height="37" rx="1.5"/>
    <line class="wick" x1="213" y1="281" x2="213" y2="319"/><rect class="candle-down" x="207" y="284" width="12" height="33" rx="1.5"/>
    <line class="wick" x1="249" y1="299" x2="249" y2="315"/><rect class="candle-down" x="243" y="302" width="12" height="11" rx="1.5"/>
    <line class="wick" x1="285" y1="333" x2="285" y2="342"/><rect class="candle-down" x="279" y="335" width="12" height="5" rx="1"/>
    <line class="wick" x1="320" y1="289" x2="320" y2="330"/><rect class="candle-down" x="314" y="291" width="12" height="36" rx="1.5"/>
    <line class="wick" x1="355" y1="310" x2="355" y2="355"/><rect class="candle-up" x="349" y="313" width="12" height="40" rx="1.5"/>
    <line class="wick" x1="390" y1="331" x2="390" y2="361"/><rect class="candle-up" x="384" y="335" width="12" height="24" rx="1.5"/>
    <line class="wick" x1="426" y1="324" x2="426" y2="361"/><rect class="candle-down" x="420" y="327" width="12" height="32" rx="1.5"/>
    <line class="wick" x1="464" y1="313" x2="464" y2="349"/><rect class="candle-down" x="458" y="316" width="12" height="31" rx="1.5"/>
    <line class="wick" x1="499" y1="306" x2="499" y2="337"/><rect class="candle-down" x="493" y="309" width="12" height="26" rx="1.5"/>
    <line class="wick" x1="536" y1="248" x2="536" y2="291"/><rect class="candle-down" x="530" y="251" width="12" height="38" rx="1.5"/>
    <line class="wick" x1="575" y1="207" x2="575" y2="257"/><rect class="candle-up" x="569" y="210" width="12" height="45" rx="1.5"/>
    <line class="wick" x1="608" y1="180" x2="608" y2="219"/><rect class="candle-up" x="602" y="183" width="12" height="34" rx="1.5"/>
    <line class="wick" x1="640" y1="209" x2="640" y2="248"/><rect class="candle-down" x="634" y="213" width="12" height="32" rx="1.5"/>
    <line class="wick" x1="676" y1="254" x2="676" y2="287"/><rect class="candle-down" x="670" y="257" width="12" height="27" rx="1.5"/>
    <line class="wick" x1="714" y1="284" x2="714" y2="309"/><rect class="candle-down" x="708" y="287" width="12" height="19" rx="1.5"/>
    <line class="wick" x1="751" y1="280" x2="751" y2="311"/><rect class="candle-down" x="745" y="283" width="12" height="26" rx="1.5"/>
    <line class="wick" x1="787" y1="252" x2="787" y2="289"/><rect class="candle-up" x="781" y="255" width="12" height="32" rx="1.5"/>
    <line class="wick" x1="823" y1="214" x2="823" y2="253"/><rect class="candle-up" x="817" y="218" width="12" height="32" rx="1.5"/>
    <line class="wick" x1="859" y1="194" x2="859" y2="234"/><rect class="candle-down" x="853" y="197" width="12" height="34" rx="1.5"/>
    <line class="wick" x1="892" y1="194" x2="892" y2="225"/><rect class="candle-down" x="886" y="197" width="12" height="25" rx="1.5"/>
    <line class="wick" x1="931" y1="221" x2="931" y2="245"/><rect class="candle-down" x="925" y="224" width="12" height="18" rx="1.5"/>
    <line class="wick" x1="967" y1="197" x2="967" y2="261"/><rect class="candle-up" x="961" y="200" width="12" height="58" rx="1.5"/>
    <line class="wick" x1="1004" y1="245" x2="1004" y2="285"/><rect class="candle-up" x="998" y="248" width="12" height="34" rx="1.5"/>
    <line class="wick" x1="1038" y1="237" x2="1038" y2="276"/><rect class="candle-down" x="1032" y="240" width="12" height="33" rx="1.5"/>
    <line class="wick" x1="1074" y1="259" x2="1074" y2="290"/><rect class="candle-down" x="1068" y="262" width="12" height="25" rx="1.5"/>
    <line class="wick" x1="1104" y1="274" x2="1104" y2="300"/><rect class="candle-down" x="1098" y="277" width="12" height="20" rx="1.5"/>
    <line class="wick" x1="1143" y1="273" x2="1143" y2="296"/><rect class="candle-down" x="1137" y="276" width="12" height="17" rx="1.5"/>
    <line class="wick" x1="1182" y1="278" x2="1182" y2="304"/><rect class="candle-down" x="1176" y="281" width="12" height="19" rx="1.5"/>
  </g>

  <path class="indicator-line" d="M70 537 L92 598 L124 605 L174 605 L200 544 L227 545 L278 590 L300 593 L365 638 L390 638 L414 643 L462 646 L496 553 L527 553 L551 529 L578 529 L601 483 L624 480 L651 524 L682 527 L733 443 L763 443 L782 398 L782 385 L815 376 Q850 410 860 465 L860 485 L895 523 L923 471 L946 488 L975 489 L1055 391 L1083 464 L1105 455 L1133 455 L1170 400 L1185 389 L1215 387"/>

  <g class="volume-bars">
    <rect x="95" y="798" width="16" height="67" rx="1.5"/><rect x="134" y="723" width="16" height="142" rx="1.5"/>
    <rect x="170" y="688" width="16" height="177" rx="1.5"/><rect x="205" y="756" width="16" height="109" rx="1.5"/>
    <rect x="241" y="739" width="16" height="126" rx="1.5"/><rect x="277" y="691" width="16" height="174" rx="1.5"/>
    <rect x="313" y="756" width="16" height="109" rx="1.5"/><rect x="347" y="713" width="16" height="152" rx="1.5"/>
    <rect x="384" y="740" width="16" height="125" rx="1.5"/><rect x="419" y="713" width="16" height="152" rx="1.5"/>
    <rect x="456" y="763" width="16" height="102" rx="1.5"/><rect x="490" y="827" width="16" height="38" rx="1.5"/>
    <rect x="526" y="802" width="16" height="63" rx="1.5"/><rect x="563" y="818" width="16" height="47" rx="1.5"/>
    <rect x="598" y="713" width="16" height="152" rx="1.5"/><rect x="633" y="697" width="16" height="168" rx="1.5"/>
    <rect x="670" y="742" width="16" height="123" rx="1.5"/><rect x="705" y="798" width="16" height="67" rx="1.5"/>
    <rect x="741" y="723" width="16" height="142" rx="1.5"/><rect x="777" y="723" width="16" height="142" rx="1.5"/>
    <rect x="812" y="798" width="16" height="67" rx="1.5"/><rect x="848" y="718" width="16" height="147" rx="1.5"/>
    <rect x="883" y="691" width="16" height="174" rx="1.5"/><rect x="919" y="723" width="16" height="142" rx="1.5"/>
    <rect x="955" y="769" width="16" height="96" rx="1.5"/><rect x="989" y="691" width="16" height="174" rx="1.5"/>
    <rect x="1025" y="818" width="16" height="47" rx="1.5"/><rect x="1062" y="838" width="16" height="27" rx="1.5"/>
    <rect x="1098" y="747" width="16" height="118" rx="1.5"/><rect x="1133" y="718" width="16" height="147" rx="1.5"/>
    <rect x="1170" y="789" width="16" height="76" rx="1.5"/>
  </g>

  <g class="time-labels">
    <text class="time-label" x="143" y="893">8 AM</text>
    <text class="time-label" x="392" y="893">9 AM</text>
    <text class="time-label" x="641" y="893">10 AM</text>
    <text class="time-label" x="893" y="893">11 AM</text>
    <text class="time-label" x="1143" y="893">12 PM</text>
  </g>
</svg>
</body>
</html>
```